Gentlemen lifestyle blog in need of a logo and webdesign

Tallbrook is a site all about tests and reviews of products for gentlemen (Gin, whiskey, barber products, outdoor equipment, tobacco, coffe and more). It will be about fashion and a luxury lifestyle, health and fitness.
it will also include a online store

```html
<!DOCTYPE html>
<html lang="en">
<head>
<meta charset="utf-8">
<title>Tallbrook — For the Modern Gentleman</title>
<link rel="stylesheet" href="https://fonts.googleapis.com/css2?family=Archivo:wght@600;700;800&family=Barlow:wght@400;500;600;700&display=swap">
<style>
:root{
  --gold:#c8964a;
  --gold-light:#e9d3ad;
  --gold-pale:#f4ead9;
  --maroon:#2b0d0c;
  --ink:#2a1210;
  --muted:#6f6461;
  --card:#f8f6f6;
  --white:#ffffff;
}
*{margin:0;padding:0;box-sizing:border-box}
html,body{width:1200px;height:3234px;overflow:hidden}
body{position:relative;background:var(--white);font-family:'Barlow',sans-serif;color:var(--ink)}
.abs{position:absolute}
.heading{font-family:'Archivo',sans-serif;font-weight:800;text-transform:uppercase;color:var(--ink)}

/* header */
.topline{left:0;top:0;width:1200px;height:4px;background:var(--gold)}
.logo{left:110px;top:30px;font-family:'Archivo',sans-serif;font-weight:800;font-size:34px;letter-spacing:1px;color:var(--maroon)}
.nav{top:40px;font-size:14px;font-weight:500;color:var(--ink)}
.icon-btn{width:44px;height:44px;border-radius:50%;background:var(--gold);display:flex;align-items:center;justify-content:center}

/* hero */
.hero{left:0;top:95px;width:1200px;height:577px;background:radial-gradient(ellipse at 30% 40%,#4a3020 0%,#23150e 45%,#120a07 100%)}
.hero-text{right:112px;text-align:right;color:var(--white)}
.eyebrow{top:191px;font-family:'Archivo',sans-serif;font-weight:700;font-size:19px}
.hero-title{top:222px;font-family:'Archivo',sans-serif;font-weight:800;font-size:55px;line-height:63px}
.hero-sub{top:360px;font-size:19px;line-height:32px;font-weight:500}
.btn{height:44px;border-radius:22px;font-weight:600;font-size:15px;display:flex;align-items:center;justify-content:center}
.btn-light{left:672px;top:445px;width:200px;background:var(--white);color:var(--gold)}
.btn-gold{left:886px;top:445px;width:202px;background:var(--gold);color:var(--white)}
.dots{left:1139px;top:309px;width:6px}
.dots span{display:block;width:5px;height:5px;border-radius:50%;background:var(--white);margin-bottom:8px}
.dots span:first-child{background:var(--gold)}

/* category strip */
.gold-rule{top:672px;height:3px;background:var(--gold)}
.gold-block{left:89px;top:674px;width:107px;height:108px;background:var(--gold)}
.cats{left:112px;top:572px;width:976px;height:188px;display:flex;box-shadow:0 10px 30px rgba(0,0,0,.08)}
.cat{flex:1;background:var(--card);text-align:center;padding-top:36px;border-right:1px solid #eee}
.cat.alt{background:var(--white)}
.cat-icon{width:60px;height:60px;margin:0 auto;border-radius:50%;background:var(--gold-pale);display:flex;align-items:center;justify-content:center}
.cat h3{margin-top:17px;font-size:16px;font-weight:600;color:#5a4a45;letter-spacing:.3px}
.cat a{display:inline-block;margin-top:7px;font-size:11px;font-weight:600;color:var(--gold);text-decoration:underline}

/* products */
.section-title{font-size:38px}
.section-sub{font-size:15px;color:#55504e}
.product{width:231px;height:311px;background:var(--white);box-shadow:0 4px 16px rgba(0,0,0,.06);text-align:center}
.product.featured{border:1px solid var(--gold-light)}
.product .photo{width:100%;height:179px}
.product.featured .photo{width:221px;margin:5px auto 0;height:170px}
.price{margin-top:24px;font-size:16px;font-weight:600;color:var(--ink)}
.pname{margin-top:6px;font-size:14px;line-height:21px;color:#6a605d}
.stars{margin-top:6px;font-size:10px;letter-spacing:1px;color:var(--gold)}
.panel{left:857px;top:939px;width:231px;height:656px;background:var(--gold);color:var(--white);padding:28px 21px}
.panel h3{font-family:'Archivo',sans-serif;font-weight:700;font-size:22px}
.panel .intro{margin-top:8px;font-size:12px;line-height:24px}
.chips{margin-top:12px;display:flex;flex-wrap:wrap;gap:12px 10px}
.chip{height:30px;border-radius:15px;background:rgba(255,255,255,.22);font-size:12px;display:flex;align-items:center;justify-content:center}
.panel hr{border:0;border-top:1px solid rgba(80,40,10,.35);margin:30px 5px 30px}
.quote{font-size:12px;line-height:24px;text-align:center}
.reviewer{text-align:center;margin-top:14px;font-size:12px;font-weight:600}
.panel .pager{display:flex;justify-content:center;gap:4px;margin-top:22px}
.panel .pager span{width:6px;height:6px;border-radius:50%;background:rgba(255,255,255,.6)}
.panel .pager span:first-child{background:var(--white)}

/* about */
.about{left:0;top:1675px;width:600px;height:514px;background:linear-gradient(135deg,#c48d3c 0%,#d7a656 55%,#bf8a3f 100%)}
.about-photo{left:600px;top:1675px;width:600px;height:514px;background:radial-gradient(ellipse at 60% 50%,#6a4018 0%,#2a1408 55%,#12091c 100%)}
.about h2{position:absolute;left:112px;top:65px;font-family:'Archivo',sans-serif;font-weight:800;font-size:38px;color:var(--white)}
.about p{position:absolute;left:112px;width:426px;font-size:15px;line-height:30px;color:var(--white);text-align:justify}
.btn-dark{left:112px;top:397px;width:136px;height:44px;border-radius:22px;background:var(--maroon);color:var(--white);font-weight:700;font-size:15px;display:flex;align-items:center;justify-content:center}

/* blogs */
.blog{width:314px;height:420px}
.blog .photo{width:314px;height:251px}
.blog .body{position:absolute;left:15px;top:198px;width:284px;height:210px;background:var(--white);box-shadow:0 6px 18px rgba(0,0,0,.06);text-align:center;padding-top:22px}
.tag{display:inline-block;height:30px;line-height:30px;padding:0 27px;border-radius:15px;background:var(--gold-pale);font-size:13px;font-weight:600;color:var(--ink)}
.blog h4{margin-top:14px;font-family:'Archivo',sans-serif;font-weight:600;font-size:14.5px;line-height:24px;text-transform:uppercase}
.blog p{margin:10px 20px 0;font-size:13px;line-height:23px;color:#786e6a}
.arrow{width:40px;height:40px;border-radius:50%;background:var(--gold-pale);display:flex;align-items:center;justify-content:center}

/* features */
.feature{top:2886px;display:flex;align-items:center}
.feature .ic{width:56px;height:56px;border-radius:50%;background:var(--gold);display:flex;align-items:center;justify-content:center;margin-right:20px}
.feature h5{font-family:'Archivo',sans-serif;font-weight:700;font-size:14px;color:var(--ink)}
.feature span{display:block;margin-top:6px;font-size:13px;color:#6a605d}

/* footer */
.footer{left:0;top:3002px;width:1200px;height:232px;background:var(--maroon);color:var(--white);text-align:center}
.footer .brand{margin-top:52px;font-family:'Archivo',sans-serif;font-weight:800;font-size:35px;letter-spacing:1px}
.footer nav{margin-top:18px;display:flex;justify-content:center;gap:52px;font-size:13px;font-weight:600}
.social{margin-top:18px;display:flex;justify-content:center;gap:5px}
.social span{width:23px;height:23px;border-radius:50%;background:var(--white)}
.copy{margin-top:14px;font-size:11px;font-weight:500}
</style>
</head>
<body>

<div class="abs topline"></div>
<div class="abs logo">TALLBROOK</div>
<div class="abs nav" style="left:452px">Home</div>
<div class="abs nav" style="left:532px">About Us</div>
<div class="abs nav" style="left:635px">Products</div>
<div class="abs nav" style="left:735px">Reviews</div>
<div class="abs nav" style="left:832px">Blogs</div>
<div class="abs nav" style="left:912px">Contact</div>
<div class="abs icon-btn" style="left:991px;top:27px">
  <svg width="14" height="14" viewBox="0 0 14 14"><circle cx="7" cy="4" r="3" fill="#fff"/><path d="M1.5 13c0-3 2.5-5 5.5-5s5.5 2 5.5 5z" fill="#fff"/></svg>
</div>
<div class="abs icon-btn" style="left:1044px;top:27px">
  <svg width="15" height="14" viewBox="0 0 15 14"><path d="M1 1.5h2l1.6 7h7.5l1.5-5H4" fill="none" stroke="#fff" stroke-width="1.6"/><circle cx="5.5" cy="12" r="1.3" fill="#fff"/><circle cx="11" cy="12" r="1.3" fill="#fff"/></svg>
</div>

<section class="abs hero" role="img" aria-label="Well-dressed gentleman relaxing in a leather armchair with a glass of whisky in a dark library"></section>
<div class="abs hero-text eyebrow">ELEVATING YOUR LIFESTYLE</div>
<h1 class="abs hero-text hero-title">FOR THE MODERN<br>GENTLEMAN</h1>
<p class="abs hero-text hero-sub">Product reviews, style tips, &amp; premium products<br>for the discerning gentleman</p>
<div class="abs btn btn-light">Join Our Community</div>
<div class="abs btn btn-gold">Explore Our Reviews</div>
<div class="abs dots"><span></span><span></span><span></span><span></span><span></span></div>

<div class="abs gold-rule" style="left:0;width:112px"></div>
<div class="abs gold-rule" style="left:1088px;width:112px"></div>
<div class="abs gold-block"></div>
<div class="abs cats">
  <div class="cat">
    <div class="cat-icon"><svg width="34" height="34" viewBox="0 0 34 34" fill="none" stroke="#c8964a" stroke-width="1.8"><rect x="6" y="6" width="8" height="22" rx="2"/><path d="M6 12l8-4M6 18l8-4M6 24l8-4M18 8l12 18M30 8L18 26"/><circle cx="18" cy="28" r="2.5"/><circle cx="30" cy="28" r="2.5"/></svg></div>
    <h3>Barber Products</h3><a>View All</a>
  </div>
  <div class="cat alt">
    <div class="cat-icon"><svg width="34" height="34" viewBox="0 0 34 34" fill="none" stroke="#c8964a" stroke-width="1.8"><path d="M20 4h5v5l3 4v17H17V13l3-4z"/><rect x="19" y="17" width="7" height="7"/><path d="M5 18h9v5a4.5 4.5 0 01-9 0z"/></svg></div>
    <h3>Gin &amp; Whiskey</h3><a>View All</a>
  </div>
  <div class="cat">
    <div class="cat-icon"><svg width="34" height="34" viewBox="0 0 34 34" fill="none" stroke="#c8964a" stroke-width="1.8"><path d="M4 28L15 10l11 18zM15 10v18M11 28l4-7 4 7M2 28h30"/><path d="M26 8v8M23 11h6"/></svg></div>
    <h3>Outdoor Equipment</h3><a>View All</a>
  </div>
  <div class="cat alt">
    <div class="cat-icon"><svg width="34" height="34" viewBox="0 0 34 34" fill="none" stroke="#c8964a" stroke-width="1.8"><path d="M17 4c3 6 3 14 0 22-3-8-3-16 0-22zM17 26c-5-3-9-8-11-14 6 2 10 7 11 14zM17 26c5-3 9-8 11-14-6 2-10 7-11 14zM17 26v5"/></svg></div>
    <h3>Tobacco &amp; Coffee</h3><a>View All</a>
  </div>
</div>

<h2 class="abs heading section-title" style="left:112px;top:840px">TOP-SELLING PRODUCTS</h2>
<p class="abs section-sub" style="left:112px;top:890px">Ut enim ad minima veniam, quis nostrum exercitationem ullam corporis suscipit laboriosam, nisi</p>

<article class="abs product" style="left:112px;top:939px">
  <div class="photo" role="img" aria-label="Shaving brush, bowl and barber tools on a wooden counter" style="background:linear-gradient(160deg,#3b2a22,#8a5a32 60%,#2a1c16)"></div>
  <div class="price">$48.00</div><div class="pname">Quis autem vel eum iure<br>reprehenderit</div><div class="stars">☆☆☆☆☆</div>
</article>
<article class="abs product featured" style="left:360px;top:939px">
  <div class="photo" role="img" aria-label="Loose tobacco leaves with rolled cigarettes" style="background:linear-gradient(160deg,#6b3a1d,#a86a3a 55%,#7d4a28)"></div>
  <div class="price">$48.00</div><div class="pname">Quis autem vel eum iure<br>reprehenderit</div><div class="stars">☆☆☆☆☆</div>
</article>
<article class="abs product" style="left:609px;top:939px">
  <div class="photo" role="img" aria-label="Camping tent, backpack and campfire in a forest at dusk" style="background:linear-gradient(160deg,#1d2a2b,#8a5a2a 55%,#1a201c)"></div>
  <div class="price">$48.00</div><div class="pname">Quis autem vel eum iure<br>reprehenderit</div><div class="stars">☆☆☆☆☆</div>
</article>
<article class="abs product" style="left:112px;top:1284px">
  <div class="photo" role="img" aria-label="Bottles of Irish whiskey on a bar shelf" style="background:linear-gradient(160deg,#3a2410,#b07a2a 50%,#2a1a0c)"></div>
  <div class="price">$48.00</div><div class="pname">Quis autem vel eum iure<br>reprehenderit</div><div class="stars">☆☆☆☆☆</div>
</article>
<article class="abs product" style="left:360px;top:1284px">
  <div class="photo" role="img" aria-label="Bottle of single malt whisky beside a filled glass" style="background:linear-gradient(160deg,#151515,#b58a3a 55%,#d8cfc0)"></div>
  <div class="price">$48.00</div><div class="pname">Quis autem vel eum iure<br>reprehenderit</div><div class="stars">☆☆☆☆☆</div>
</article>
<article class="abs product" style="left:609px;top:1284px">
  <div class="photo" role="img" aria-label="Espresso grinder filling a portafilter with ground coffee" style="background:linear-gradient(160deg,#0f0f10,#6a4a36 55%,#1c1816)"></div>
  <div class="price">$48.00</div><div class="pname">Quis autem vel eum iure<br>reprehenderit</div><div class="stars">☆☆☆☆☆</div>
</article>

<aside class="abs panel">
  <h3>CATEGORIES</h3>
  <p class="intro">Ut enim ad minima veniam, quis nostrum exercitationem ullam corporis suscipit labor</p>
  <div class="chips">
    <span class="chip" style="width:66px">Coffee</span>
    <span class="chip" style="width:104px">Whiskey</span>
    <span class="chip" style="width:125px">Barber products</span>
    <span class="chip" style="width:45px">Gin</span>
    <span class="chip" style="width:180px">Outdoor equipment</span>
    <span class="chip" style="width:91px">Tobacco</span>
    <span class="chip" style="width:75px">More •••</span>
  </div>
  <hr>
  <p class="quote">Neque porro quisquam est, qui dolorem ipsum quia dolor sit amet, consectetur, adipisci velit, sed quia non numquam eius modi tempora incidunt ut labore et dolore magnam aliquam quaerat voluptatem.</p>
  <div class="reviewer"><span style="letter-spacing:1px">★★★★☆</span><br>MARCUS VALE</div>
  <div class="pager"><span></span><span></span><span></span><span></span></div>
</aside>

<section class="abs about">
  <h2>ABOUT US</h2>
  <p style="top:125px">Ut enim ad minima veniam, quis nostrum exercitationem ullam corporis suscipit laboriosam, nisi ut aliquid ex ea commodi consequatur?</p>
  <p style="top:230px">Nemo enim ipsam voluptatem quia voluptas sit aspernatur aut odit aut fugit, sed quia consequuntur magni dolores eos qui ratione voluptatem sequi nesciunt. Neque porro quisquam est, qui dolorem ipsum quia dolor sit amet, consectetur, adipisci velit, sed quia non numquam.</p>
  <div class="abs btn-dark">Read More</div>
</section>
<div class="abs about-photo" role="img" aria-label="Crystal whisky decanter and glasses on a velvet case by candlelight"></div>

<h2 class="abs heading section-title" style="left:0;width:1200px;text-align:center;top:2258px">LATEST BLOGS</h2>
<p class="abs section-sub" style="left:0;width:1200px;text-align:center;top:2308px">Ut enim ad minima veniam, quis nostrum exercitationem ullam corporis suscipit laboriosam, nisi</p>

<article class="abs blog" style="left:112px;top:2353px">
  <div class="photo" role="img" aria-label="Man in a beige suit holding a phone in a modern lounge" style="background:linear-gradient(160deg,#1f2a2c,#5a4030 55%,#2a2522)"></div>
  <div class="body"><span class="tag">luxury lifestyle</span><h4>UT ENIM AD MINIMA VENIAM,<br>QUIS NOSTRUM EXER</h4><p>Ut enim ad minima veniam, quis nostrum exercitationem ullam corporis suscipit laboriosam</p></div>
</article>
<article class="abs blog" style="left:443px;top:2353px">
  <div class="photo" role="img" aria-label="Couple relaxing on a sofa surrounded by plants" style="background:linear-gradient(160deg,#4a6a3a,#9aa6a8 55%,#5a6a6c)"></div>
  <div class="body"><span class="tag">Health</span><h4>UT ENIM AD MINIMA VENIAM,<br>QUIS NOSTRUM EXER</h4><p>Ut enim ad minima veniam, quis nostrum exercitationem ullam corporis suscipit laboriosam</p></div>
</article>
<article class="abs blog" style="left:774px;top:2353px">
  <div class="photo" role="img" aria-label="Man running on a treadmill in a bright gym" style="background:linear-gradient(160deg,#d8d2c8,#8a8480 55%,#3a3634)"></div>
  <div class="body"><span class="tag">Fitness</span><h4>UT ENIM AD MINIMA VENIAM,<br>QUIS NOSTRUM EXER</h4><p>Ut enim ad minima veniam, quis nostrum exercitationem ullam corporis suscipit laboriosam</p></div>
</article>

<div class="abs arrow" style="left:556px;top:2794px"><svg width="12" height="10" viewBox="0 0 12 10" fill="none" stroke="#c8964a" stroke-width="1.6"><path d="M6 1L2 5l4 4M10 1L6 5l4 4"/></svg></div>
<div class="abs arrow" style="left:604px;top:2794px"><svg width="12" height="10" viewBox="0 0 12 10" fill="none" stroke="#c8964a" stroke-width="1.6"><path d="M2 1l4 4-4 4M6 1l4 4-4 4"/></svg></div>

<div class="abs feature" style="left:131px">
  <div class="ic"><svg width="28" height="28" viewBox="0 0 28 28" fill="none" stroke="#fff" stroke-width="1.6"><circle cx="14" cy="14" r="11"/><circle cx="14" cy="14" r="7"/><path d="M10.5 14l2.5 2.5 4.5-5"/></svg></div>
  <div><h5>TOP QUALITY</h5><span>Reprehenderit qui in ea voluptate</span></div>
</div>
<div class="abs feature" style="left:461px">
  <div class="ic"><svg width="28" height="28" viewBox="0 0 28 28" fill="none" stroke="#fff" stroke-width="1.6"><path d="M5 16v-3a9 9 0 0118 0v3"/><rect x="3" y="15" width="5" height="7" rx="2"/><rect x="20" y="15" width="5" height="7" rx="2"/><path d="M23 22c0 3-4 4-8 4"/></svg></div>
  <div><h5>CUSTOMER SUPPORT</h5><span>Reprehenderit qui in ea voluptate</span></div>
</div>
<div class="abs feature" style="left:791px">
  <div class="ic"><svg width="28" height="28" viewBox="0 0 28 28" fill="none" stroke="#fff" stroke-width="1.6"><rect x="4" y="8" width="20" height="14" rx="2"/><path d="M4 12h20M8 18h5"/><circle cx="19" cy="17" r="2.5"/></svg></div>
  <div><h5>SECURE PAYMENT</h5><span>Reprehenderit qui in ea voluptate</span></div>
</div>

<footer class="abs footer">
  <div class="brand">TALLBROOK</div>
  <nav><span>HOME</span><span>ABOUT US</span><span>PRODUCTS</span><span>REVIEWS</span><span>BLOGS</span><span>CONTACT US</span></nav>
  <div class="social"><span></span><span></span><span></span><span></span><span></span><span></span><span></span><span></span></div>
  <div class="copy">(C) Copyright | All Rights Reserved</div>
</footer>

</body>
</html>
```